Finely Larder Packaging Design - Flexible Packaging FFS- form, fill and seal

looking for a universal packaging for my brand of products which include nuts,seed,spices, dried fruits etc
We have had this contest before but we need something more fresh n upmarket
The packets will be displayed on supermarket shelves and have to be very high end packaging
The packed product must be clearly visible both front and back of the packets
preferred colours are maroon, gold outline.
the bottom of the packet we want a theme in green colour related to a farm/ orchard/ valley, instead of the Indian design on attached sample design from QT packet
the new design should be oriented around the QT sample packet images attached herein
the white centre part on the QT packet is where the product information will be printed using laser jet in printer it wil include, product name , expiry date, bar code , weight etc

the back of the design must include following logos
1)recycle, 2)RAMO standardization mark, 3)TLP logo, 4)Swiss certification,5)keep city clean logo, 6) halal logo
also look for ideas from www.kollandrift.de & www.zimmaqo.ae
the final design should clearly communicate an upmarket packaging that expresses quality products.
the finely larder current logo colours can be changed to maroon and gold. black colour is also welcome on the packaging design.

Target Market(s)

high ned supermarkets, focus on packing a quality packaging

Industry/Entity Type

Printer

Requirements
Must have
• maroon , gold colour, clear fonts must be used

```html
<!DOCTYPE html>
<html lang="en">
<head>
<meta charset="utf-8">
<title>Finely Larder – Flexible Pack</title>
<link href="https://fonts.googleapis.com/css2?family=Josefin+Sans:wght@400;600&display=swap" rel="stylesheet">
<style>
  :root{
    --stage-top:#8e0a10;
    --stage:#b10f17;
    --maroon:#c1121c;
    --gold:#d9b24a;
    --gold-deep:#a87d22;
    --ink:#141414;
    --band:#1b1b1b;
    --band-soft:#3a3a3a;
    --window-light:#ecd7a6;
    --window-mid:#d9b26e;
    --window-dark:#b9863f;
    --field-light:#a6d45a;
    --field-mid:#6fae2f;
    --field-dark:#3f7f1d;
    --label-edge:#8cc63f;
    --paper:#ffffff;
    --text:#1a1a1a;
    --badge:#cfcfcf;
  }
  *{margin:0;padding:0;box-sizing:border-box}
  html,body{width:1200px;height:1000px;overflow:hidden}
  body{background:radial-gradient(ellipse at 50% 45%,var(--stage) 0%,var(--stage-top) 100%);
    font-family:"Josefin Sans",sans-serif;position:relative}

  .artwork{position:absolute;inset:0}

  .brand-text{position:absolute;display:flex;flex-direction:column;align-items:center;justify-content:center;text-align:center}
  .brand-dot{border-radius:50%;background:var(--maroon)}
  .brand-name{color:var(--maroon);font-weight:600;line-height:1.05}

  .brand-text--hero{left:500px;top:40px;width:236px;height:200px;gap:10px}
  .brand-text--hero .brand-dot{width:60px;height:60px}
  .brand-text--hero .brand-name{font-size:36px}

  .brand-text--front{left:268px;top:350px;width:194px;height:172px;gap:10px}
  .brand-text--front .brand-dot{width:50px;height:50px}
  .brand-text--front .brand-name{font-size:32px}

  .brand-text--back{left:721px;top:348px;width:116px;height:114px;gap:6px}
  .brand-text--back .brand-dot{width:28px;height:28px}
  .brand-text--back .brand-name{font-size:18px}

  .info-label{position:absolute;left:216px;top:712px;width:170px;height:112px;color:var(--text)}
  .info-label h2{font-weight:400;font-size:31px;letter-spacing:.5px;line-height:1}
  .info-label .facts{font-size:11px;line-height:1.2;margin-top:6px;padding-left:4px}
  .info-label .origin{font-size:11px;line-height:1.2;margin-top:8px}
</style>
</head>
<body>

<svg class="artwork" width="1200" height="1000" viewBox="0 0 1200 1000">
  <defs>
    <linearGradient id="gold-rim" x1="0" y1="0" x2="1" y2="1">
      <stop offset="0" stop-color="#f2d27a"/><stop offset=".5" stop-color="var(--gold)"/><stop offset="1" stop-color="var(--gold-deep)"/>
    </linearGradient>
    <linearGradient id="nuts" x1="0" y1="0" x2="1" y2="1">
      <stop offset="0" stop-color="var(--window-light)"/><stop offset=".55" stop-color="var(--window-mid)"/><stop offset="1" stop-color="var(--window-dark)"/>
    </linearGradient>
    <linearGradient id="band" x1="0" y1="0" x2="1" y2="0">
      <stop offset="0" stop-color="var(--band)"/><stop offset=".5" stop-color="var(--band-soft)"/><stop offset="1" stop-color="var(--band)"/>
    </linearGradient>
    <linearGradient id="field" x1="0" y1="0" x2="0" y2="1">
      <stop offset="0" stop-color="var(--field-light)"/><stop offset=".5" stop-color="var(--field-mid)"/><stop offset="1" stop-color="var(--field-dark)"/>
    </linearGradient>
    <linearGradient id="gloss" x1="0" y1="0" x2="1" y2="0">
      <stop offset="0" stop-color="#fff" stop-opacity="0"/><stop offset=".5" stop-color="#fff" stop-opacity=".22"/><stop offset="1" stop-color="#fff" stop-opacity="0"/>
    </linearGradient>
    <linearGradient id="edge-shade" x1="0" y1="0" x2="1" y2="0">
      <stop offset="0" stop-color="#000" stop-opacity=".28"/><stop offset=".12" stop-color="#000" stop-opacity="0"/>
      <stop offset=".88" stop-color="#000" stop-opacity="0"/><stop offset="1" stop-color="#000" stop-opacity=".28"/>
    </linearGradient>
    <linearGradient id="reflect" x1="0" y1="0" x2="0" y2="1">
      <stop offset="0" stop-color="#000" stop-opacity=".25"/><stop offset="1" stop-color="#000" stop-opacity="0"/>
    </linearGradient>
    <clipPath id="bag-front"><path d="M138 266H588V296Q572 600 588 926V940H138V926Q156 600 138 296Z"/></clipPath>
    <clipPath id="bag-back"><path d="M652 266H1100V296Q1086 600 1100 926V940H652V926Q668 600 652 296Z"/></clipPath>
  </defs>

  <!-- hero brand panel -->
  <path class="brand-panel" d="M504 44Q540 44 548 16Q618 0 688 16Q696 44 732 44V246H504Z"
        fill="var(--ink)" stroke="url(#gold-rim)" stroke-width="6" stroke-linejoin="round"/>

  <!-- floor reflections -->
  <rect x="138" y="942" width="450" height="58" fill="url(#reflect)"/>
  <rect x="652" y="942" width="448" height="58" fill="url(#reflect)"/>

  <!-- front packet -->
  <g clip-path="url(#bag-front)">
    <rect x="138" y="266" width="450" height="674" fill="url(#nuts)" role="img" aria-label="Clear window showing roasted peanuts"/>
    <path d="M138 266H588V420Q420 430 300 436Q210 440 138 446Z" fill="url(#band)" role="img" aria-label="Dark swirl and leaf pattern band"/>
    <path d="M138 812Q260 800 400 812Q440 760 500 762Q540 790 588 800V940H138Z" fill="url(#field)" role="img" aria-label="Green farm fields with barn"/>
    <rect x="138" y="266" width="450" height="24" fill="#000" opacity=".25"/>
    <rect x="138" y="918" width="450" height="22" fill="#000" opacity=".18"/>
    <rect x="190" y="296" width="38" height="620" fill="url(#gloss)"/>
    <rect x="138" y="266" width="450" height="674" fill="url(#edge-shade)"/>
  </g>
  <path d="M268 344Q288 344 294 334H436Q442 344 462 344V528H268Z"
        fill="var(--ink)" stroke="url(#gold-rim)" stroke-width="5" stroke-linejoin="round"/>
  <path class="info-label-card" d="M208 708Q300 690 393 700V830H208Z"
        fill="var(--paper)" stroke="var(--label-edge)" stroke-width="5" stroke-linejoin="round"/>

  <!-- back packet -->
  <g clip-path="url(#bag-back)">
    <rect x="652" y="266" width="448" height="674" fill="url(#nuts)" role="img" aria-label="Clear window showing roasted peanuts"/>
    <path d="M652 266H1100V366Q980 392 840 384Q740 386 652 404Z" fill="url(#band)" role="img" aria-label="Dark swirl and leaf pattern band"/>
    <path d="M652 830Q700 780 760 772Q820 800 900 834Q1000 826 1100 838V940H652Z" fill="url(#field)" role="img" aria-label="Green farm fields with barn"/>
    <rect x="652" y="266" width="448" height="24" fill="#000" opacity=".25"/>
    <rect x="652" y="918" width="448" height="22" fill="#000" opacity=".18"/>
    <rect x="846" y="266" width="40" height="674" fill="url(#gloss)"/>
    <rect x="652" y="266" width="448" height="674" fill="url(#edge-shade)"/>
  </g>
  <path d="M720 344Q732 344 736 336H822Q826 344 838 344V466H720Z"
        fill="var(--ink)" stroke="url(#gold-rim)" stroke-width="4" stroke-linejoin="round"/>

  <!-- certification marks -->
  <g class="cert-panel" aria-label="Certification marks">
    <rect x="912" y="768" width="134" height="64" rx="6" fill="var(--paper)"/>
    <circle cx="930" cy="786" r="10" fill="var(--badge)"/>
    <circle cx="964" cy="786" r="10" fill="var(--badge)"/>
    <circle cx="998" cy="786" r="10" fill="var(--badge)"/>
    <rect x="1020" y="776" width="18" height="20" rx="2" fill="var(--badge)"/>
    <rect x="920" y="804" width="18" height="20" rx="2" fill="var(--badge)"/>
    <rect x="950" y="808" width="28" height="10" rx="2" fill="var(--badge)"/>
    <circle cx="998" cy="814" r="10" fill="var(--badge)"/>
  </g>
</svg>

<div class="brand-text brand-text--hero">
  <span class="brand-dot"></span>
  <span class="brand-name">Finely<br>Larder</span>
</div>

<div class="brand-text brand-text--front">
  <span class="brand-dot"></span>
  <span class="brand-name">Finely<br>Larder</span>
</div>

<div class="brand-text brand-text--back">
  <span class="brand-dot"></span>
  <span class="brand-name">Finely<br>Larder</span>
</div>

<div class="info-label">
  <h2>PEANUTS</h2>
  <p class="facts">NET WEIGHT.: 150 g<br>BEST BEFORE: 5/7/15</p>
  <p class="origin">PRODUCT<br>OF XXXXX</p>
</div>

</body>
</html>
```